Membership Drive "CHRISTMAS SPECIAL"

Looking to run a "Christmas Special" on 6 month Memberships for December 2019 to boost membership number up. This is a great time to get people exercising and everyone loves a Christmas Sale. Special is designed to attract more people to join and enjoy the savings.
Artwork will be display via social media (FB and Instagram) as well as in store. Artwork must be eye catching and direct to the customer. Customer should feel a sense of relief with being able to exercise at a lower cost .

Heading: "Christmas Sale"
6 Months
$199.00 Save over 30%
Terms and conditions apply"
*Offer End 31st December

below are other promos we had designed on Sketch Harbor along with potential photos to be included into this promo

Target Market(s)

Males and Females aged between 16 - 45

Industry/Entity Type

Fitness

Colors

Designer to choose colors to be used in the design.

Requirements
Must have
• Must emphasize "Christmas Special" $199.00 Save over 30%
• Terms and conditions apply
• Offer Ends 31st of December
• "All of our contact details"
• Address: 14 Wattle Rd Brindle Park 3187
• Ph: 9472 6158
• www.ironpulsefit.com.au
• Design format must come in PDF for a AO poster and an Instagram format please
Nice to have
• Some Christmas feels to the artwork

```html
<!DOCTYPE html>
<html lang="en">
<head>
<meta charset="utf-8">
<title>Christmas Sale – Ironpulse</title>
<link href="https://fonts.googleapis.com/css2?family=Lilita+One&family=Fjalla+One&family=Montserrat:wght@700;800;900&family=Open+Sans:wght@700&display=swap" rel="stylesheet">
<style>
  :root {
    --red-bright: #e3262b;
    --red-mid: #c8141c;
    --red-deep: #7d0b10;
    --white: #ffffff;
    --yellow: #fff200;
    --ink: #111111;
    --green: #2f7d1f;
    --green-deep: #215c14;
    --green-text: #3c8a22;
    --sky-light: #d8ecf8;
    --sky-mid: #8fbfe0;
    --hair: #6a4430;
  }
  html, body {
    margin: 0;
    padding: 0;
    overflow: hidden;
    background: #ffffff;
  }
  .poster {
    position: relative;
    width: 831px;
    height: 1200px;
    overflow: hidden;
    background: radial-gradient(ellipse at 50% 45%, var(--red-bright) 0%, var(--red-mid) 55%, var(--red-deep) 100%);
    font-family: "Montserrat", sans-serif;
  }
  .headline-box {
    position: absolute;
    left: 72px;
    top: 39px;
    width: 680px;
    height: 296px;
    border: 6px solid var(--white);
    background: var(--red-mid);
    box-shadow: 0 4px 14px rgba(0,0,0,0.25);
    text-align: center;
  }
  .headline {
    margin: 0;
    font-family: "Lilita One", sans-serif;
    font-weight: 400;
    color: var(--white);
    text-transform: uppercase;
    text-shadow: 4px 5px 0 #a80d14, 6px 8px 0 rgba(0,0,0,0.2);
    letter-spacing: 1px;
  }
  .headline-top { font-size: 128px; line-height: 1; padding-top: 16px; }
  .headline-bottom { font-size: 138px; line-height: 1; margin-top: -4px; }

  .photo-ring {
    position: absolute;
    left: 72px;
    top: 282px;
    width: 686px;
    height: 686px;
    border-radius: 50%;
    background: radial-gradient(circle, rgba(120,6,12,0) 60%, rgba(90,4,10,0.55) 72%, rgba(90,4,10,0) 80%);
  }
  .photo {
    position: absolute;
    left: 97px;
    top: 307px;
    width: 636px;
    height: 636px;
    border-radius: 50%;
    background:
      radial-gradient(ellipse 45% 60% at 50% 70%, rgba(106,68,48,0.55), rgba(106,68,48,0) 70%),
      radial-gradient(circle at 50% 30%, var(--sky-light), var(--sky-mid));
  }
  .duration {
    position: absolute;
    top: 366px;
    left: 0;
    width: 831px;
    text-align: center;
    font-family: "Lilita One", sans-serif;
    font-size: 70px;
    color: var(--green-text);
    -webkit-text-stroke: 8px var(--white);
    paint-order: stroke fill;
    text-shadow: 0 3px 6px rgba(0,0,0,0.35);
    letter-spacing: 1px;
  }
  .green-band {
    position: absolute;
    left: 0;
    top: 900px;
    width: 831px;
    height: 300px;
  }
  .offer {
    position: absolute;
    left: 0;
    width: 831px;
    text-align: center;
    margin: 0;
  }
  .price {
    top: 806px;
    font-family: "Lilita One", sans-serif;
    font-size: 58px;
    color: var(--yellow);
    -webkit-text-stroke: 7px var(--ink);
    paint-order: stroke fill;
    left: -55px;
  }
  .saving {
    top: 868px;
    font-family: "Lilita One", sans-serif;
    font-size: 62px;
    color: var(--yellow);
    -webkit-text-stroke: 7px var(--ink);
    paint-order: stroke fill;
    left: -8px;
  }
  .terms {
    top: 945px;
    font-family: "Fjalla One", sans-serif;
    font-size: 33px;
    color: var(--yellow);
    -webkit-text-stroke: 5px var(--ink);
    paint-order: stroke fill;
    left: -10px;
  }
  .deadline {
    top: 1000px;
    font-family: "Montserrat", sans-serif;
    font-weight: 800;
    font-size: 33px;
    color: var(--white);
    -webkit-text-stroke: 5px var(--ink);
    paint-order: stroke fill;
    left: -10px;
  }
  .contact {
    position: absolute;
    left: 32px;
    top: 1092px;
    margin: 0;
    font-family: "Open Sans", sans-serif;
    font-weight: 700;
    font-size: 18px;
    line-height: 29px;
    color: var(--white);
    font-style: normal;
  }
  .brand {
    position: absolute;
    left: 520px;
    top: 1080px;
    width: 270px;
    text-align: center;
    font-family: "Montserrat", sans-serif;
    font-weight: 900;
    font-size: 46px;
    color: var(--white);
    margin: 0;
  }
</style>
</head>
<body>
  <main class="poster">
    <div class="headline-box">
      <h1 class="headline headline-top">Christmas</h1>
      <p class="headline headline-bottom">Sale</p>
    </div>

    <div class="photo-ring"></div>
    <div class="photo" role="img" aria-label="Smiling woman in a Santa hat holding a red and white gift box against a pale blue sky"></div>

    <p class="duration">6 MONTHS</p>

    <svg class="green-band" viewBox="0 0 831 300" aria-hidden="true">
      <path d="M0 135 Q 420 90 831 0 L831 300 L0 300 Z" fill="var(--green)"/>
      <path d="M0 135 Q 420 90 831 0 L831 10 Q 420 100 0 145 Z" fill="var(--green-deep)" opacity="0.6"/>
    </svg>

    <p class="offer price">$199.00</p>
    <p class="offer saving">Save over 30%</p>
    <p class="offer terms">Terms and conditions apply</p>
    <p class="offer deadline">Offer End 31st December</p>

    <address class="contact">
      Address: 14 Wattle Rd Brindle Park 3187<br>
      Ph: 9472 6158<br>
      www.ironpulsefit.com.au
    </address>

    <p class="brand">IRONPULSE</p>
  </main>
</body>
</html>
```